Etiketten für Imkerei
Zielgruppe
Wir sind eine Imkerei in München. Die Zielgrppe sind Menschen, die lokale Produkte wertschätzen, beim Produzenten gern direkt und auf Märkten einkaufen.
Hallo,
wir benötigen ein universelles Design für Honiggläser-Etiketten, das für verschiedene Sorten verwendet werden kann. Das vorhanden Logo soll im Design aufgenommen werden. Im Logo reicht der Name: Imkerei-Brunntal.

```html
<!DOCTYPE html>
<html lang="de">
<head>
<meta charset="utf-8">
<title>Waldhonig – Etikett Imkerei Brunntal</title>
<link rel="stylesheet" href="https://fonts.googleapis.com/css2?family=Source+Sans+3:ital,wght@0,400;0,600;0,700;1,700&family=Dancing+Script:wght@500&family=Allura&display=swap">
<style>
  :root {
    --honey: #fecc00;
    --ink: #0f0f0f;
    --leaf: #1f7a38;
    --paper: #ffffff;
    --bee-tone: #e8b800;
  }
  * { margin: 0; padding: 0; box-sizing: border-box; }
  html, body { width: 849px; height: 1200px; overflow: hidden; background: var(--paper); }
  body { position: relative; font-family: "Source Sans 3", sans-serif; }

  .label {
    position: absolute; left: 120px; top: 115px;
    width: 613px; height: 289px;
    background: var(--honey);
  }
  .label__band {
    position: absolute; left: 0; top: 0; width: 100%; height: 110px;
    background: var(--ink);
  }
  .label__frame { position: absolute; left: 186px; top: 15px; width: 252px; height: 258px; }

  .web {
    position: absolute; left: 22px; top: 83px;
    color: var(--honey); font-weight: 700; font-size: 11px;
  }

  .brand {
    position: absolute; left: 236px; top: 50px; width: 130px;
    display: flex; align-items: center; gap: 8px;
    color: var(--paper); font-weight: 600; font-size: 15px; line-height: 1.05;
  }
  .brand__mark { width: 18px; height: 18px; border: 2px solid var(--paper); flex: none; }

  .weight {
    position: absolute; left: 548px; top: 50px;
    color: var(--honey); font-weight: 700; font-style: italic; font-size: 13px;
  }

  .bee { position: absolute; border-radius: 45%; }
  .bee--weight { left: 527px; top: 27px; width: 30px; height: 30px; background: var(--bee-tone); opacity: .8; }
  .bee--address { left: 82px; top: 160px; width: 38px; height: 38px; background: #3a3000; opacity: .35; }
  .bee--hero { left: 315px; top: 120px; width: 84px; height: 78px; background: radial-gradient(circle, #fff7d0 0%, #fff2b0 55%, var(--honey) 100%); }

  .address {
    position: absolute; left: 22px; top: 196px;
    color: var(--ink); font-size: 10.5px; line-height: 13.7px;
  }
  .address strong { font-weight: 700; }

  .variety {
    position: absolute; left: 210px; top: 176px;
    transform: rotate(-8deg); transform-origin: left center;
    font-family: "Dancing Script", cursive; font-size: 38px; color: var(--ink); line-height: 1;
  }
  .tagline {
    position: absolute; left: 282px; top: 203px;
    transform: rotate(-8deg); transform-origin: left center;
    color: var(--leaf); font-weight: 700; font-size: 11.5px;
  }

  .side {
    position: absolute; right: 19px; top: 184px; width: 150px; text-align: right;
  }
  .side__title { font-family: "Allura", cursive; font-size: 19px; color: var(--ink); line-height: 1.1; }
  .side__text { margin-top: 8px; color: var(--leaf); font-size: 9px; line-height: 11.5px; }
</style>
</head>
<body>
  <section class="label" aria-label="Honigglas-Etikett Waldhonig">
    <div class="label__band"></div>

    <svg class="label__frame" viewBox="0 0 252 258" aria-hidden="true">
      <polyline points="4,95 4,4 248,4 248,95" fill="none" stroke="var(--honey)" stroke-width="4"/>
      <polyline points="4,95 4,254 248,254 248,95" fill="none" stroke="var(--ink)" stroke-width="4"/>
    </svg>

    <p class="web">www.imkerei-brunntal.de</p>

    <div class="brand">
      <span class="brand__mark"></span>
      <span>Imkerei Brunntal</span>
    </div>

    <div class="bee bee--weight" role="img" aria-label="Kleine Biene"></div>
    <p class="weight">500 gr</p>

    <div class="bee bee--address" role="img" aria-label="Kleine Biene"></div>
    <p class="address">
      <strong>Imkerei Brunntal</strong><br>
      Tobias Brenner<br>
      Lindenweg 14<br>
      81245 München<br>
      Tel.: 0049-(0)176 482 115 09<br>
      info@imkerei-brunntal.de
    </p>

    <div class="bee bee--hero" role="img" aria-label="Fliegende Biene, weiße Illustration"></div>
    <h1 class="variety">Waldhonig</h1>
    <p class="tagline">Qualität aus der Region</p>

    <div class="side">
      <p class="side__title">Flüssiger Waldhonig</p>
      <p class="side__text">Mit Beginn der Holunderblüte<br>ziehen die Völker in Waldgebiete<br>um, danach dem besonderen<br>Waldhonig zu gehen.</p>
    </div>
  </section>
</body>
</html>
```